ARC VOLLEY Business Card Project

I'd like to request a business card design for the new company I've launched.
The name of the company is "ARC VOLLEY" an indoor unmanned tennis practice facility.
We would like to see designs that use our brand identity color in the logo I've attached.
We hope to get the design with modern, luxurious and elegant tone and manner.
We hope the logo should not be too big.

Business card must have elements as below:
- Logo (One of the logos I've attached)
- Name (In Korean Text) : 박 서 윤
- Title (In Korean Text) : 대표
- Phone Number : 010-8472-3916
- Email Address : seoyun.park@arcvolley-example.co.kr
- Website : www.arcvolley-example.co.kr
- Instagram : arcvolley
- Address (In Korean text) : 경기도 용인시 수지구 풍덕천로 456 미래타워 5층 501호, 502호

Target Market(s)

Tennis amateurs in 20 to 40s

Industry/Entity Type

Sports, Hobby

Contact Information for Business Card

- Logo (One of the logos I've attached) - Name (In Korean Text) : 박 서 윤 - Title (In Korean Text) : 대표 - Phone Number : 010-8472-3916 - Email Address : seoyun.park@arcvolley-example.co.kr - Website : www.arcvolley-example.co.kr - Instagram : arcvolley - Address (In Korean text) : 경기도 용인시 수지구 풍덕천로 456 미래타워 5층 501호, 502호

Font styles to use
Sans Serif

Requirements
Must have
• Double sided
Nice to have
• Logo with intaglio or relief embossing
Should not have
• Logo should not be too big.

```html
<!DOCTYPE html>
<html lang="ko">
<head>
<meta charset="UTF-8">
<title>ARC VOLLEY Business Card</title>
<link rel="stylesheet" href="https://fonts.googleapis.com/css2?family=Cinzel:wght@500&family=Noto+Sans+KR:wght@300;400&family=Open+Sans:wght@600&display=swap">
<style>
  :root {
    --green-deep: #0f5a32;
    --green-mid: #17703c;
    --green-shadow: #1a4a28;
    --green-back: #1f5c35;
    --racket-pale: #dfe4f2;
    --racket-blue: #aab6de;
    --ink-dark: #1d3a25;
    --white: #ffffff;
  }
  * { margin: 0; padding: 0; box-sizing: border-box; }
  html, body { width: 1199px; height: 1200px; overflow: hidden; background: var(--white); }
  .canvas { position: relative; width: 1199px; height: 1200px; }

  .card {
    position: absolute; width: 687px; height: 392px; overflow: hidden;
    background:
      linear-gradient(135deg, transparent 40%, rgba(255,255,255,0.04) 40%, rgba(255,255,255,0.04) 55%, transparent 55%),
      linear-gradient(135deg, transparent 65%, rgba(0,0,0,0.06) 65%, rgba(0,0,0,0.06) 78%, transparent 78%),
      linear-gradient(135deg, var(--green-deep) 0%, var(--green-mid) 50%, var(--green-deep) 100%);
  }
  .card-front { left: 259px; top: 230px; }
  .card-back { left: 255px; top: 635px; background:
      linear-gradient(135deg, transparent 30%, rgba(255,255,255,0.04) 30%, rgba(255,255,255,0.04) 45%, transparent 45%),
      linear-gradient(135deg, var(--green-back) 0%, #23643a 60%, var(--green-back) 100%); }

  .illustration-area {
    position: absolute;
    background: linear-gradient(135deg, var(--green-shadow) 0%, #5f8a78 50%, var(--racket-pale) 100%);
    opacity: 0.55;
  }
  .card-front .illustration-area { left: 0; top: 100px; width: 307px; height: 292px; }
  .card-back .illustration-area { left: 0; top: 0; width: 187px; height: 190px; }

  .brand-name {
    position: absolute; font-family: 'Cinzel', serif; font-weight: 500;
    color: var(--white); letter-spacing: 1px; white-space: nowrap;
  }
  .card-front .brand-name { left: 368px; top: 52px; font-size: 38px; }

  .person-name {
    position: absolute; left: 380px; width: 258px; top: 200px; text-align: center;
    font-family: 'Noto Sans KR', sans-serif; font-weight: 300; font-size: 62px;
    color: var(--white); line-height: 1;
  }
  .person-title {
    position: absolute; left: 380px; width: 258px; top: 290px; text-align: center;
    font-family: 'Noto Sans KR', sans-serif; font-weight: 400; font-size: 29px;
    color: var(--white); line-height: 1;
  }

  .silver-panel { position: absolute; inset: 0; }

  .contact-row {
    position: absolute; display: flex; align-items: center; justify-content: flex-end;
    font-family: 'Open Sans', sans-serif; font-weight: 600; font-size: 14px;
    color: var(--white); white-space: nowrap;
  }
  .contact-row .label { margin-right: 9px; text-align: right; }
  .contact-row .label.address { font-family: 'Noto Sans KR', sans-serif; font-weight: 400; font-size: 15.5px; line-height: 1.3; }
  .icon-box {
    width: 36px; height: 36px; background: var(--ink-dark);
    border-radius: 3px 8px 3px 8px; display: flex; align-items: center; justify-content: center;
    box-shadow: 2px 2px 0 #5aa048;
  }
  .icon-box svg { width: 20px; height: 20px; fill: var(--white); }

  .back-mark {
    position: absolute; left: 478px; top: 202px; width: 84px; height: 84px;
    border-radius: 50%; background: var(--ink-dark);
  }
  .card-back .brand-name { left: 412px; top: 290px; width: 224px; text-align: center; font-size: 30px; color: var(--ink-dark); }
</style>
</head>
<body>
<div class="canvas">

  <section class="card card-front">
    <div class="illustration-area" role="img" aria-label="Illustration of a white tennis racket with strings and a dark green shadow"></div>
    <div class="brand-name">ARC VOLLEY</div>
    <div class="person-name">박 서 윤</div>
    <div class="person-title">대표</div>
  </section>

  <section class="card card-back">
    <div class="illustration-area" role="img" aria-label="Illustration of a tennis racket handle and a green tennis ball"></div>

    <svg class="silver-panel" viewBox="0 0 687 392" preserveAspectRatio="none" aria-hidden="true">
      <defs>
        <linearGradient id="silver" x1="0" y1="0" x2="1" y2="1">
          <stop offset="0" stop-color="#b9babd"/>
          <stop offset="0.5" stop-color="#f4f4f5"/>
          <stop offset="0.75" stop-color="#c7c8cb"/>
          <stop offset="1" stop-color="#eeeeef"/>
        </linearGradient>
      </defs>
      <polygon points="242,392 625,9 687,68 687,392" fill="url(#silver)"/>
    </svg>

    <div class="contact-row" style="right:229px; top:120px;">
      <span class="label address">경기도 용인시 수지구 풍덕천로<br>456 미래타워 5층 501호, 502호</span>
      <span class="icon-box"><svg viewBox="0 0 24 24"><path d="M12 2a7 7 0 0 0-7 7c0 5 7 13 7 13s7-8 7-13a7 7 0 0 0-7-7zm0 9.5A2.5 2.5 0 1 1 12 6.5a2.5 2.5 0 0 1 0 5z"/></svg></span>
    </div>
    <div class="contact-row" style="right:266px; top:168px;">
      <span class="label">SEOYUN.PARK@ARCVOLLEY-EXAMPLE.CO.KR</span>
      <span class="icon-box"><svg viewBox="0 0 24 24"><path d="M3 5h18v2l-9 6-9-6z M3 9l9 6 9-6v10H3z"/></svg></span>
    </div>
    <div class="contact-row" style="right:301px; top:204px;">
      <span class="label">010-8472-3916</span>
      <span class="icon-box"><svg viewBox="0 0 24 24"><path d="M6.6 10.8a15 15 0 0 0 6.6 6.6l2.2-2.2a1 1 0 0 1 1-.25 11.4 11.4 0 0 0 3.6.57 1 1 0 0 1 1 1V20a1 1 0 0 1-1 1A17 17 0 0 1 3 4a1 1 0 0 1 1-1h3.5a1 1 0 0 1 1 1c0 1.25.2 2.45.57 3.6a1 1 0 0 1-.25 1z"/></svg></span>
    </div>
    <div class="contact-row" style="right:337px; top:240px;">
      <span class="label">ARCVOLLEY</span>
      <span class="icon-box"><svg viewBox="0 0 24 24"><circle cx="12" cy="12" r="6"/></svg></span>
    </div>
    <div class="contact-row" style="right:373px; top:278px;">
      <span class="label">WWW.ARCVOLLEY-EXAMPLE.CO.KR</span>
      <span class="icon-box"><svg viewBox="0 0 24 24"><path d="M12 2a10 10 0 1 0 0 20 10 10 0 0 0 0-20zm0 2c1.3 1.6 2.2 3.8 2.4 7H9.6c.2-3.2 1.1-5.4 2.4-7zM4.1 13h3.5c.1 2.4.6 4.4 1.4 6A8 8 0 0 1 4.1 13zm0-2A8 8 0 0 1 9 5c-.8 1.6-1.3 3.6-1.4 6zm5.5 2h4.8c-.2 3.2-1.1 5.4-2.4 7-1.3-1.6-2.2-3.8-2.4-7zm6.8 0h3.5a8 8 0 0 1-4.9 6c.8-1.6 1.3-3.6 1.4-6zm0-2c-.1-2.4-.6-4.4-1.4-6a8 8 0 0 1 4.9 6z"/></svg></span>
    </div>

    <div class="back-mark" aria-hidden="true"></div>
    <div class="brand-name">ARC VOLLEY</div>
  </section>

</div>
</body>
</html>
```